kel varnto website design

An IT support and IT Security Company - just use dummy text for now for the design. Examples of sites we like the looks and feel of but need it more professional feel are like: www.brovaquent.uk.com , www.plimdore.co.uk, www.quastenvel.com/professional/, www.vio.com, www.mulvex.com,

Best to message me if you have any questions

Target Market(s)

small to medium UK based companies that require IT support services

Industry/Entity Type

It Company

Contact Information for Business Card

use dummy name, telephone and email for now, will provide details later.

Logo Text

kel varnto (and then below the logo it should say "your IT, networks and security partner")

Coding

Coded - Design and coding required

Number of Pages Required

5+ page

Colors

Designer to choose colors to be used in the design.

Requirements
Must have
• must be professional, yet simple and clear that this is a serious IT support and IT security company.
Nice to have
• 1)The website homepage must have professional quality pictures of IT support or London city skyline or any picture that projects friendly business partners, professionalism and ready to serve.
• 2) Home page needs to include tabs for following pages 'Services' , 'About Us' , 'Contact Us' 'Home'
• 3) Website built customised using wordpress is ideal and easy for us to manage.
• more room for boxed options from homepage (with pic or image in background)
Should not have
• no checkout trolleys or payment options.

```html
<!DOCTYPE html>
<html lang="en">
<head>
<meta charset="utf-8">
<title>Kel Varnto – IT Support &amp; Security</title>
<link href="https://fonts.googleapis.com/css2?family=Open+Sans:ital,wght@0,300;0,400;0,600;1,400&family=Roboto:wght@300;400;500&display=swap" rel="stylesheet">
<style>
:root{
  --teal:#2fb3b9;
  --teal-dark:#1f8f96;
  --teal-deep:#0f5f66;
  --footer:#124d55;
  --footer-bottom:#0d3d44;
  --ink:#333;
  --muted:#777;
  --light:#f4f4f4;
  --orange:#e8822a;
  --white:#fff;
}
*{box-sizing:border-box;margin:0;padding:0}
html,body{width:1200px;height:4314px;overflow:hidden}
body{font-family:"Open Sans",Arial,sans-serif;color:var(--ink);background:var(--white);position:relative}
.abs{position:absolute}
.topbar{top:0;left:0;width:1200px;height:40px;background:var(--teal);color:var(--white);font-size:13px}
.topbar .social{left:86px;top:13px;display:flex;gap:12px}
.topbar .social span{width:14px;height:14px;background:rgba(255,255,255,.85);border-radius:2px}
.topbar .mail{left:255px;top:11px}
.topbar .phone{left:520px;top:11px}
.topbar .search{left:940px;top:0;width:260px;height:40px;background:var(--teal-dark);padding:11px 0 0 60px;opacity:.9}
.nav{top:40px;left:0;width:1200px;height:110px;background:var(--white)}
.logo{left:74px;top:30px}
.logo .name{font-family:"Roboto",sans-serif;font-weight:500;font-size:24px;color:var(--teal);line-height:1.1;display:flex;align-items:center;gap:12px}
.logo .mark{width:22px;height:22px;background:var(--teal)}
.logo .tagline{font-size:12px;color:var(--muted);margin-top:6px;letter-spacing:.2px}
.menu{right:60px;top:46px;display:flex;gap:46px;font-size:13px;font-family:"Roboto",sans-serif}
.menu a{color:var(--ink);text-decoration:none}
.menu a.active{color:var(--teal)}
.hero{top:150px;left:0;width:1200px;height:585px;background:linear-gradient(180deg,#4fb2c8 0%,#3c97ad 55%,#2f7f93 100%)}
.hero .kicker{left:150px;top:150px;color:var(--white);font-size:22px;font-family:"Roboto",sans-serif}
.hero h1{left:150px;top:180px;font-family:"Roboto",sans-serif;font-weight:300;font-size:40px;color:var(--white);background:rgba(255,255,255,.15);padding:0 10px 0 0}
.hero p{left:150px;top:238px;width:480px;color:var(--white);font-size:15px;line-height:1.45}
.hero .btns{left:150px;top:325px;display:flex;gap:24px}
.btn-ghost{border:2px solid var(--white);color:var(--white);border-radius:24px;font-size:13px;padding:12px 30px}
.hero .arrow{top:270px;width:22px;height:22px;border-radius:50%;background:rgba(255,255,255,.5)}
.hero .dots{left:570px;top:570px;display:flex;gap:8px}
.hero .dots span{width:10px;height:10px;border-radius:50%;border:2px solid var(--teal);background:var(--white)}
.section-title{width:1200px;text-align:center;font-family:"Roboto",sans-serif;font-weight:300;font-size:30px;color:var(--ink)}
.rule{width:40px;height:3px;background:var(--teal);left:580px}
.service{width:290px;text-align:center}
.service .icon{width:110px;height:110px;border-radius:50%;background:#f6f6f6;box-shadow:0 0 0 6px #fafafa;margin:0 auto;display:flex;align-items:center;justify-content:center}
.service h3{font-family:"Roboto",sans-serif;font-weight:500;font-size:18px;margin-top:26px;color:var(--ink)}
.service p{font-size:13px;color:var(--muted);line-height:1.5;margin:8px auto 0;width:270px}
.btn-outline{display:inline-block;border:2px solid var(--teal);color:var(--teal);border-radius:22px;font-size:12px;padding:10px 22px;margin-top:22px}
.infra{top:1625px;left:0;width:1200px;height:325px;background:linear-gradient(90deg,#e9eef1 0%,#d7e1e6 50%,#b9c9d1 100%);text-align:center}
.infra h2{margin-top:88px;font-family:"Roboto",sans-serif;font-weight:300;font-size:38px;color:var(--teal)}
.infra p{width:620px;margin:10px auto 0;font-size:18px;line-height:1.4;color:#444}
.infra .chev{left:584px;top:310px;width:32px;height:32px;border-radius:50%;background:var(--white)}
.feature h3{font-family:"Roboto",sans-serif;font-weight:400;font-size:20px;color:var(--ink)}
.feature .lead{font-style:italic;font-size:14px;color:var(--muted);line-height:1.5;margin-top:18px;width:480px}
.feature ul{list-style:none;margin-top:16px}
.feature li{font-size:13px;color:var(--muted);display:flex;gap:12px;margin-bottom:16px;width:420px;line-height:1.4}
.feature li svg{flex:none;margin-top:2px}
.photo{border-radius:2px}
.news{width:242px;height:193px}
.partners{top:3337px;left:0;width:1200px;height:144px;display:flex;justify-content:center;align-items:center;gap:70px}
.partners span{width:110px;height:44px;background:#d5d8db;border-radius:4px}
.quote{top:3481px;left:0;width:1200px;height:365px;background:linear-gradient(135deg,#3bbfc4 0%,#2aa9b0 50%,#238f98 100%)}
.quote h2{top:62px;width:1200px;text-align:center;color:var(--white);font-family:"Roboto",sans-serif;font-weight:300;font-size:32px}
.field{color:var(--white);font-size:13px;border-bottom:1px solid rgba(255,255,255,.7);padding-bottom:8px;width:260px}
.textarea{left:340px;top:165px;width:520px;height:88px;background:rgba(255,255,255,.2);color:var(--white);font-size:13px;padding:14px}
.send{left:540px;top:270px;width:118px;height:36px;background:var(--orange);color:var(--white);font-size:13px;text-align:center;line-height:36px}
.testimonial{top:3846px;left:0;width:1200px;height:110px;background:var(--teal-deep)}
.testimonial .avatar{left:110px;top:-30px;width:125px;height:125px;border-radius:50%;border:4px solid var(--white);background:linear-gradient(180deg,#c9c3bd,#8c8580)}
.testimonial p{left:355px;top:34px;color:var(--white);font-style:italic;font-weight:600;font-size:19px;line-height:1.4}
.testimonial .qmark{left:310px;top:28px;color:var(--white);font-size:46px;font-family:Georgia,serif;line-height:1}
.footer{top:3956px;left:0;width:1200px;height:302px;background:var(--footer);color:var(--white)}
.footer h4{font-family:"Roboto",sans-serif;font-weight:400;font-size:19px}
.footer ul{list-style:none;margin-top:24px}
.footer li{font-size:13px;margin-bottom:7px;color:#dce9eb}
.contact-row{display:flex;gap:14px;font-size:13px;color:#dce9eb;margin-top:14px;line-height:1.4}
.contact-row i{flex:none;width:20px;height:20px;border-radius:50%;background:var(--white);display:flex;align-items:center;justify-content:center}
.follow{display:flex;gap:12px;margin-top:26px}
.follow span{width:30px;height:30px;border-radius:50%;background:var(--white)}
.bottombar{top:4258px;left:0;width:1200px;height:56px;background:var(--footer-bottom);color:#bcd2d5;font-size:13px;padding:20px 0 0 100px}
</style>
</head>
<body>

<header class="abs topbar">
  <div class="abs social"><span></span><span></span><span></span></div>
  <div class="abs mail">info@kelvarnto.com</div>
  <div class="abs phone">020-7946-0318</div>
  <div class="abs search">Search...</div>
</header>

<nav class="abs nav">
  <div class="abs logo">
    <div class="name"><span>KEL VARNTO</span><span class="mark"></span></div>
    <div class="tagline">your IT, networks and security partner</div>
  </div>
  <div class="abs menu">
    <a class="active" href="#">HOME</a><a href="#">ABOUT US</a><a href="#">SERVICES</a><a href="#">RESOURCES</a><a href="#">CONTACT US</a>
  </div>
</nav>

<section class="abs hero" role="img" aria-label="London riverside skyline with clock tower and river boat, tinted teal">
  <div class="abs kicker">WHO WE ARE</div>
  <h1 class="abs">KEL VARNTO, IT SPECIALISTS</h1>
  <p class="abs">Lorem Ipsum is simply dummy text of the printing and typesetting industry. dummy text ever since the 1500s, when an unknown printer took a galley of type and specimen book.</p>
  <div class="abs btns"><span class="btn-ghost">CONTACT US</span><span class="btn-ghost">READ MORE</span></div>
  <span class="abs arrow" style="left:66px"></span>
  <span class="abs arrow" style="left:1110px"></span>
  <div class="abs dots"><span></span><span></span><span></span></div>
</section>

<h2 class="abs section-title" style="top:822px">OUR SERVICES</h2>
<div class="abs rule" style="top:872px"></div>

<div class="abs service" style="left:143px;top:938px">
  <div class="icon"><svg width="50" height="40" viewBox="0 0 50 40"><rect x="4" y="24" width="8" height="14" fill="#2fb3b9"/><rect x="16" y="18" width="8" height="20" fill="#2fb3b9"/><rect x="28" y="12" width="8" height="26" fill="#2fb3b9"/><rect x="40" y="6" width="8" height="32" fill="#2fb3b9"/></svg></div>
  <h3>IT FINANCIAL SERVICES</h3>
  <p>There are many variations of passages of Lorem Ipsum available...</p>
  <span class="btn-outline">READ MORE</span>
</div>
<div class="abs service" style="left:453px;top:938px">
  <div class="icon"><svg width="46" height="46" viewBox="0 0 46 46"><path d="M8 38 L38 8 M8 8 L38 38" stroke="#2fb3b9" stroke-width="6" stroke-linecap="round"/></svg></div>
  <h3>IT SUPPORT SERVICES</h3>
  <p>There are many variations of passages of Lorem Ipsum available...</p>
  <span class="btn-outline">READ MORE</span>
</div>
<div class="abs service" style="left:764px;top:938px">
  <div class="icon"><svg width="50" height="46" viewBox="0 0 50 46"><circle cx="25" cy="8" r="6" fill="#2fb3b9"/><circle cx="8" cy="36" r="6" fill="#2fb3b9"/><circle cx="25" cy="36" r="6" fill="#2fb3b9"/><circle cx="42" cy="36" r="6" fill="#2fb3b9"/><path d="M25 14v16M25 22H8v8M25 22h17v8" stroke="#2fb3b9" stroke-width="2" fill="none"/></svg></div>
  <h3>OUTSOURCED SERVICE</h3>
  <p>There are many variations of passages of Lorem Ipsum available...</p>
  <span class="btn-outline">READ MORE</span>
</div>
<div class="abs service" style="left:143px;top:1248px">
  <div class="icon"><svg width="50" height="40" viewBox="0 0 50 40"><rect x="6" y="26" width="6" height="12" fill="#2fb3b9"/><rect x="16" y="20" width="6" height="18" fill="#2fb3b9"/><rect x="26" y="14" width="6" height="24" fill="#2fb3b9"/><rect x="36" y="8" width="6" height="30" fill="#2fb3b9"/><path d="M4 20 L20 10 L30 14 L46 2" stroke="#2fb3b9" stroke-width="2" fill="none"/></svg></div>
  <h3>B2B ANALYTICS</h3>
  <p>There are many variations of passages of Lorem Ipsum available...</p>
  <span class="btn-outline">READ MORE</span>
</div>
<div class="abs service" style="left:453px;top:1248px">
  <div class="icon"><svg width="48" height="46" viewBox="0 0 48 46"><circle cx="24" cy="12" r="8" fill="#2fb3b9"/><path d="M10 40 Q24 14 38 40Z" fill="#2fb3b9"/><path d="M4 30h40" stroke="#2fb3b9" stroke-width="2"/></svg></div>
  <h3>IT CONSULTANCY</h3>
  <p>There are many variations of passages of Lorem Ipsum available...</p>
  <span class="btn-outline">READ MORE</span>
</div>

<section class="abs infra" role="img" aria-label="Business people reviewing documents, softly faded background">
  <h2>Business Infrastructure</h2>
  <p>It is a long established fact that a reader will be distracted by the readable content of a page when looking at its layout.</p>
  <span class="abs chev"></span>
</section>

<div class="abs photo" style="left:86px;top:2014px;width:484px;height:345px;background:linear-gradient(135deg,#9aa7b3,#5d6b78)" role="img" aria-label="Speaker presenting to a seated business audience"></div>
<div class="abs feature" style="left:633px;top:2046px">
  <h3>Lorem Ipsum is simply dummy text of the printing?</h3>
  <p class="lead">There are many variations of passages of Lorem Ipsum available, but the majority have suffered alteration in some form.</p>
  <ul>
    <li><svg width="14" height="12" viewBox="0 0 14 12"><path d="M1 6l4 4 8-9" stroke="#2fb3b9" stroke-width="2.5" fill="none"/></svg>Lorem Ipsum is simply dummy text</li>
    <li><svg width="14" height="12" viewBox="0 0 14 12"><path d="M1 6l4 4 8-9" stroke="#2fb3b9" stroke-width="2.5" fill="none"/></svg>It is a long established fact that a reader will be distracted</li>
    <li><svg width="14" height="12" viewBox="0 0 14 12"><path d="M1 6l4 4 8-9" stroke="#2fb3b9" stroke-width="2.5" fill="none"/></svg>Contrary to popular belief, Lorem Ipsum is not simply random text</li>
  </ul>
  <span class="btn-outline" style="margin-top:10px">READ MORE</span>
</div>

<div class="abs" style="top:2417px;left:0;width:1200px;height:460px;background:var(--light)"></div>
<div class="abs feature" style="left:86px;top:2506px">
  <h3>Lorem Ipsum is simply dummy text of the printing?</h3>
  <p class="lead">There are many variations of passages of Lorem Ipsum available, but the majority have suffered alteration in some form.</p>
  <ul>
    <li><svg width="14" height="12" viewBox="0 0 14 12"><path d="M1 6l4 4 8-9" stroke="#2fb3b9" stroke-width="2.5" fill="none"/></svg>Lorem Ipsum is simply dummy text</li>
    <li><svg width="14" height="12" viewBox="0 0 14 12"><path d="M1 6l4 4 8-9" stroke="#2fb3b9" stroke-width="2.5" fill="none"/></svg>It is a long established fact that a reader will be distracted</li>
    <li><svg width="14" height="12" viewBox="0 0 14 12"><path d="M1 6l4 4 8-9" stroke="#2fb3b9" stroke-width="2.5" fill="none"/></svg>Contrary to popular belief, Lorem Ipsum is not simply random text</li>
  </ul>
  <span class="btn-outline" style="margin-top:10px">READ MORE</span>
</div>
<div class="abs photo" style="left:627px;top:2480px;width:486px;height:340px;background:linear-gradient(135deg,#d8dde2,#7b8794)" role="img" aria-label="Two businessmen in suits reviewing a tablet together"></div>

<h2 class="abs section-title" style="top:2942px">NEWS INSIGHTS</h2>
<div class="abs rule" style="top:2992px"></div>
<div class="abs news" style="left:86px;top:3061px;background:linear-gradient(135deg,#c7c9cb,#7d8185)" role="img" aria-label="Business team meeting around a desk"></div>
<div class="abs news" style="left:348px;top:3061px;background:linear-gradient(135deg,#b7c7d4,#5d7385)" role="img" aria-label="Smiling businessman in front of colleagues"></div>
<div class="abs news" style="left:610px;top:3061px;background:linear-gradient(180deg,#9fb8cc,#56677a)" role="img" aria-label="City office towers against the sky"></div>
<div class="abs news" style="left:872px;top:3061px;background:linear-gradient(135deg,#d9dadc,#8e9297)" role="img" aria-label="Colleagues in a bright conference room"></div>

<div class="abs partners">
  <span></span><span></span><span></span><span></span><span></span><span></span>
</div>

<section class="abs quote">
  <h2 class="abs">REQUEST A QUOTE</h2>
  <div class="abs field" style="left:340px;top:128px">Name</div>
  <div class="abs field" style="left:600px;top:128px">Email</div>
  <div class="abs textarea">Enter your message</div>
  <div class="abs send">SEND</div>
</section>

<section class="abs testimonial">
  <div class="abs avatar" role="img" aria-label="Portrait of a smiling support agent"></div>
  <div class="abs qmark">“</div>
  <p class="abs">Ready to see how marketing automation can help you grow at record speeds?<br>Request a personalized demo today!</p>
</section>

<footer class="abs footer">
  <div class="abs" style="left:110px;top:50px">
    <h4>Quick links</h4>
    <ul><li>Home</li><li>About Us</li><li>Services</li><li>Resources</li><li>Contact Us</li></ul>
  </div>
  <div class="abs" style="left:318px;top:50px">
    <h4>Resources</h4>
    <ul><li>IT Services Data Sheet</li><li>Managed IT Support Data Sheet</li><li>Business Continuity Checklist</li></ul>
  </div>
  <div class="abs" style="left:636px;top:50px">
    <h4>Contact us</h4>
    <div class="contact-row"><i><svg width="10" height="12" viewBox="0 0 10 12"><path d="M5 0a4 4 0 0 0-4 4c0 3 4 8 4 8s4-5 4-8a4 4 0 0 0-4-4z" fill="#124d55"/></svg></i><span>Level 11, 48 Harlow Street<br>Brenford VICTORIA 1234</span></div>
    <div class="contact-row"><i><svg width="10" height="10" viewBox="0 0 10 10"><path d="M2 0h2l1 3-1.5 1a6 6 0 0 0 2.5 2.5L7 5l3 1v2c0 1-1 2-2 2A8 8 0 0 1 0 2c0-1 1-2 2-2z" fill="#124d55"/></svg></i><span>CALL US<br>020-7946-0427</span></div>
    <div class="contact-row"><i><svg width="12" height="9" viewBox="0 0 12 9"><rect x="0.5" y="0.5" width="11" height="8" fill="none" stroke="#124d55"/><path d="M0.5 0.5l5.5 4 5.5-4" stroke="#124d55" fill="none"/></svg></i><span>info@kelvarnto.com</span></div>
  </div>
  <div class="abs" style="left:942px;top:50px">
    <h4>Follow us on</h4>
    <div class="follow"><span></span><span></span><span></span><span></span></div>
  </div>
</footer>
<div class="abs bottombar">© 2017 Kel Varnto. All Rights Reserved</div>

</body>
</html>
```